Create Vertical Dog Food Labels (3 inches x 5 inches) for PupKitchen

We need a packing Vertical label (3 inches x 5 inches) design for our line of Dog Food - Pup Kitchen at pupkitchenmeals.com (please review website). This design is for Custom Roll Labels. We have a logo already. Use our logo colors on label. What we need incorporated is a list of our ingredients:

50% Choice Beef
20% Pasture-raised Chicken
15% Brown Rice
15% Fresh Vegetables - Carrots, Kale, Zucchini
Herbal Health Boosters

We also need these lines at the bottom of the label:

Keeps in fridge for 4 days after thawing
Stores in freezer up to 6 months
Questions? email us at orders@meadowlanepantry.com

We have attached a sample of a competitor. The Kibble Crate.

Target Market(s)

Dog owners

Industry/Entity Type

Dog Food

Font styles to use
Sans Serif

Requirements
Must have
• Read project description above
Nice to have
• Our logo color incorporated
Should not have
• I want it simple.

```html
<!DOCTYPE html>
<html lang="en">
<head>
<meta charset="utf-8">
<title>PupKitchen – Vertical Dog Food Labels</title>
<link rel="stylesheet" href="https://fonts.googleapis.com/css2?family=Poppins:wght@400;600&display=swap">
<style>
  :root {
    --backdrop: #0a6608;
    --paper: #ffffff;
    --green-ink: #0b6a0b;
    --green-tint: #d3e3d5;
    --orange-ink: #f4592a;
    --orange-tint: #fde0d8;
  }
  * { box-sizing: border-box; margin: 0; padding: 0; }
  html, body { width: 1200px; height: 1200px; overflow: hidden; }
  body {
    background: var(--backdrop);
    font-family: "Poppins", sans-serif;
    position: relative;
  }
  .label {
    position: absolute;
    top: 264px;
    width: 403px;
    height: 671px;
    background: var(--paper);
    overflow: hidden;
  }
  .label--green { left: 147px; color: var(--green-ink); }
  .label--orange { left: 650px; color: var(--orange-ink); }

  .paw-art {
    position: absolute;
    border-radius: 46% 46% 50% 50%;
  }
  .label--green .paw-art { background: var(--green-tint); }
  .label--orange .paw-art { background: var(--orange-tint); }
  .paw-art--top { left: 9px; top: 21px; width: 72px; height: 75px; }
  .paw-art--right { left: 311px; top: 60px; width: 100px; height: 132px; }
  .paw-art--left { left: -10px; top: 255px; width: 96px; height: 120px; }

  .brand {
    position: absolute;
    left: 0; right: 0; top: 87px;
    display: flex; flex-direction: column; align-items: center;
  }
  .brand__mark {
    width: 138px; height: 138px; border-radius: 50%;
  }
  .label--green .brand__mark { background: var(--green-tint); }
  .label--orange .brand__mark { background: var(--orange-tint); }
  .brand__name {
    margin-top: 8px;
    font-size: 34px; font-weight: 600; color: var(--green-ink);
    letter-spacing: 0.5px;
  }

  .ingredients {
    position: absolute;
    left: 33px; width: 339px; top: 381px;
    font-size: 15.5px; line-height: 20px;
  }
  .ingredient {
    display: flex; justify-content: space-between; align-items: center;
    border-bottom: 1.5px solid currentColor;
    padding: 0 15px 0 2px;
    height: 27px;
  }
  .ingredient--tall { height: 47px; }
  .ingredient__share { flex: none; }
  .ingredient--boosters { border-bottom: none; height: 25px; }
  .boosters-bar { height: 13px; background: currentColor; border-radius: 2px; }

  .storage {
    position: absolute;
    left: 31px; width: 341px; top: 569px; height: 71px;
    border: 1.5px solid currentColor;
    display: flex; flex-direction: column; justify-content: center; align-items: center;
    font-size: 15.5px; font-weight: 600; line-height: 21px;
    white-space: nowrap;
  }
  .contact {
    position: absolute;
    left: 0; right: 0; top: 647px;
    text-align: center;
    font-size: 12px; line-height: 16px;
    white-space: nowrap;
  }
</style>
</head>
<body>

  <section class="label label--green">
    <div class="paw-art paw-art--top" role="img" aria-label="faint paw print decoration"></div>
    <div class="paw-art paw-art--right" role="img" aria-label="faint paw print decoration"></div>
    <div class="paw-art paw-art--left" role="img" aria-label="faint paw print decoration"></div>
    <div class="brand">
      <div class="brand__mark"></div>
      <div class="brand__name">PupKitchen</div>
    </div>
    <div class="ingredients">
      <div class="ingredient"><span>Choice Beef</span><span class="ingredient__share">50%</span></div>
      <div class="ingredient"><span>Pasture-raised Chicken</span><span class="ingredient__share">20%</span></div>
      <div class="ingredient"><span>Brown Rice</span><span class="ingredient__share">15%</span></div>
      <div class="ingredient ingredient--tall"><span>Fresh Vegetables -<br>Carrots, Kale, Zucchini</span><span class="ingredient__share">15%</span></div>
      <div class="ingredient ingredient--boosters"><span>Herbal Health Boosters</span></div>
      <div class="boosters-bar"></div>
    </div>
    <div class="storage">
      <p>* Keeps in fridge for 4 days after thawing</p>
      <p>* Stores in freezer up to 6 months</p>
    </div>
    <p class="contact">Questions? email us at orders@meadowlanepantry.com</p>
  </section>

  <section class="label label--orange">
    <div class="paw-art paw-art--top" role="img" aria-label="faint paw print decoration"></div>
    <div class="paw-art paw-art--right" role="img" aria-label="faint paw print decoration"></div>
    <div class="paw-art paw-art--left" role="img" aria-label="faint paw print decoration"></div>
    <div class="brand">
      <div class="brand__mark"></div>
      <div class="brand__name">PupKitchen</div>
    </div>
    <div class="ingredients">
      <div class="ingredient"><span>Choice Beef</span><span class="ingredient__share">50%</span></div>
      <div class="ingredient"><span>Pasture-raised Chicken</span><span class="ingredient__share">20%</span></div>
      <div class="ingredient"><span>Brown Rice</span><span class="ingredient__share">15%</span></div>
      <div class="ingredient ingredient--tall"><span>Fresh Vegetables -<br>Carrots, Kale, Zucchini</span><span class="ingredient__share">15%</span></div>
      <div class="ingredient ingredient--boosters"><span>Herbal Health Boosters</span></div>
      <div class="boosters-bar"></div>
    </div>
    <div class="storage">
      <p>* Keeps in fridge for 4 days after thawing</p>
      <p>* Stores in freezer up to 6 months</p>
    </div>
    <p class="contact">Questions? email us at orders@meadowlanepantry.com</p>
  </section>

</body>
</html>
```